Professional business cards for real estate development company

I need business cards for my new real estate development company. The company, "KORVA" is a real estate development, investment, and advisory firm with a focus on multifamily, office, and mixed-use projects across primary and secondary markets in the Southeast United States.

Style preference is modern

Industry/Entity Type

Real Estate Development

Contact Information for Business Card

The business cards need to include:
Name
Title
Mailing Address
Phone Number
Web Address

Logo is attached. I would like white to be the primary color with incorporation of the company colors: #232D3A and #B5A451

Font styles to use
Other font styles liked:
• Montserrat, Avenir

Requirements
Must have
• Company Logo. No need to include the company name since the name is in the logo.
Should not have
• No line type designs

```html
<!DOCTYPE html>
<html lang="en">
<head>
<meta charset="utf-8">
<title>KORVA Business Card</title>
<link rel="stylesheet" href="https://fonts.googleapis.com/css2?family=Poppins:wght@400;500;700&display=swap">
<style>
  :root {
    --page-bg: #e9e6e1;
    --card-dark: #15181e;
    --ink: #232d3a;
    --ink-soft: #2e333b;
    --gold: #b5a451;
    --icon-fg: #e9e6e1;
  }
  * { margin: 0; padding: 0; box-sizing: border-box; }
  html, body {
    width: 1200px;
    height: 970px;
    overflow: hidden;
    background: var(--page-bg);
    font-family: "Poppins", sans-serif;
  }
  .card {
    position: absolute;
    left: 70px;
    top: 182px;
    width: 1060px;
    height: 606px;
    background: var(--card-dark);
    overflow: hidden;
    box-shadow: 0 18px 40px rgba(0,0,0,0.18);
  }
  .card-wave {
    position: absolute;
    inset: 0;
    width: 100%;
    height: 100%;
  }
  .brand {
    position: absolute;
    left: 650px;
    top: 196px;
    display: flex;
    align-items: center;
    gap: 18px;
  }
  .brand-mark {
    width: 26px;
    height: 26px;
    background: var(--gold);
  }
  .brand-name {
    font-weight: 500;
    font-size: 84px;
    line-height: 1;
    letter-spacing: 2px;
    color: var(--ink);
  }
  .contact {
    position: absolute;
    left: 50px;
    top: 262px;
    color: var(--ink-soft);
  }
  .person-name {
    font-weight: 700;
    font-size: 31px;
    line-height: 1.1;
    color: var(--ink);
    letter-spacing: 0.3px;
  }
  .person-title {
    font-size: 23px;
    line-height: 1.3;
  }
  .address {
    margin-top: 26px;
    font-size: 23px;
    line-height: 1.35;
  }
  .lines {
    margin-top: 16px;
    list-style: none;
    font-size: 24px;
    line-height: 34px;
  }
  .lines li {
    display: flex;
    align-items: center;
    gap: 12px;
  }
  .icon {
    width: 24px;
    height: 24px;
    flex: none;
  }
</style>
</head>
<body>
  <div class="card">
    <svg class="card-wave" viewBox="0 0 1060 606" preserveAspectRatio="none" aria-hidden="true">
      <defs>
        <linearGradient id="frost" x1="0" y1="0" x2="1" y2="1">
          <stop offset="0" stop-color="#e6e2dc"/>
          <stop offset="0.3" stop-color="#f3f6fa"/>
          <stop offset="0.6" stop-color="#dcdfe4"/>
          <stop offset="0.8" stop-color="#c9c2ba"/>
          <stop offset="1" stop-color="#b9b4ae"/>
        </linearGradient>
        <radialGradient id="warm" cx="0.28" cy="0.9" r="0.25">
          <stop offset="0" stop-color="#e7b9bd" stop-opacity="0.7"/>
          <stop offset="1" stop-color="#e7b9bd" stop-opacity="0"/>
        </radialGradient>
      </defs>
      <path d="M0,234 C270,80 630,18 1060,12 L1060,258 C940,468 540,548 0,580 Z" fill="url(#frost)"/>
      <path d="M0,234 C270,80 630,18 1060,12 L1060,258 C940,468 540,548 0,580 Z" fill="url(#warm)"/>
    </svg>

    <div class="brand">
      <span class="brand-mark"></span>
      <span class="brand-name">KORVA</span>
    </div>

    <div class="contact">
      <div class="person-name">DANIEL R. HOLT</div>
      <div class="person-title">Executive Director</div>
      <div class="address">PO BOX418 Magnolia Ave<br>Suite 210 Atlanta,USA</div>
      <ul class="lines">
        <li>
          <svg class="icon" viewBox="0 0 24 24" aria-hidden="true">
            <circle cx="12" cy="12" r="12" fill="#232d3a"/>
            <path d="M8.5 6.5l2 2.6-1.2 1.4c.8 1.7 2.1 3 3.8 3.8l1.4-1.2 2.6 2-1.2 2c-4.6-.3-8.6-4.3-8.9-8.9z" fill="#e9e6e1"/>
          </svg>
          <span>404-555-0187</span>
        </li>
        <li>
          <svg class="icon" viewBox="0 0 24 24" aria-hidden="true">
            <circle cx="12" cy="12" r="12" fill="#232d3a"/>
            <rect x="6" y="8" width="12" height="8.5" fill="none" stroke="#e9e6e1" stroke-width="1.5"/>
            <path d="M6 8l6 5 6-5" fill="none" stroke="#e9e6e1" stroke-width="1.5"/>
          </svg>
          <span>info@korvamail.com</span>
        </li>
        <li>
          <svg class="icon" viewBox="0 0 24 24" aria-hidden="true">
            <circle cx="12" cy="12" r="12" fill="#232d3a"/>
            <circle cx="12" cy="12" r="6" fill="none" stroke="#e9e6e1" stroke-width="1.3"/>
            <ellipse cx="12" cy="12" rx="2.6" ry="6" fill="none" stroke="#e9e6e1" stroke-width="1.2"/>
            <path d="M6 12h12" stroke="#e9e6e1" stroke-width="1.2"/>
          </svg>
          <span>www.korvadev.com</span>
        </li>
      </ul>
    </div>
  </div>
</body>
</html>
```